依頼詳細
①去年のチラシデータを添付させていただきました。
②今年はコンクールが中止となったため、写真は昨年の中央の時の写真と、アンサンブルコンテスト支部大会の写真を入れていただきたいです。
③部活のロゴがあるので、それもどこかに入れていただきたいです。
④観客は保護者のみなので、場所の地図は不要です。
⑤公式VIDORAチャンネルのQRコードはどこかに入れてほしいです。
⑥ここ数年緑や茶色などが多かったので、ピンク、赤、青などの色で作ってみたいです。イメージは特にありません。あまりに子供っぽいものは好きではないです。

・今回のデータをDVDジャケットに転用させていただきますのでよろしくお願い申し上げます。

よろしくお願い致します。
記載項目
札幌市立柳浦中学校吹奏楽部
第12回定期演奏会
【無観客演奏会~保護者、関係者のみ人数を制限して入場しています。】
11月1日(日)13:00開場 13:30開演 15:00終演予定
場所:ヒバリノ会館(札幌紅葉アリーナ)
主催:札幌市立柳浦中学校 吹奏楽部保護者会
●プログラム

〇第43回中央室内楽フェスタ演奏予定曲
「砂丘の鐘と港の夜明け」~木管8重奏バージョン~Tovelu作曲
〇ウィンディ・ハーバー「舟と小夜子の夢渡り」より
〇ボルディエット
〇元気200km
〇サクソフォンとバンドのための夏空の約束~ミルバーンズ 永遠のレパートリーより~
〇風を追って走ろうよ in swing
ほか

☆VIDORA無料ライブ配信~札幌市立柳浦中学校吹奏楽部公式チャンネルにて!
☆お問い合わせ 札幌市立柳浦中学校 鹿間・楢戸・砂川(011-555-0178)
☆今回の定期演奏会は、新型コロナウイルス感染予防防止の観点から、保護者・学校関係者のみの公演となりました。

サイズ
A4
ページ数
片面
希望イメージ
シンプル 複雑
単色 カラフル
暗い 明るい
日常 高級
遊び心 厳粛
未来的 伝統的
女性的 男性的
希望する色
赤系、青系
納品ファイル
• 高解像度JPG (.jpg)
• PNG形式 (.png)
補足説明
ファイルはよくわからないのですが、プリモスなどの印刷会社に200枚程度の印刷をお願いするのと、Chirpzaやホームページにチラシ画像を貼る予定です。どのファイル形式がよいかは教えてください。
Vidoraでのライブ配信の部分が目立つようにしてほしいです。今回は一般の方に会場に来ていただくことはできないので、Vidoraを出来るだけたくさんの方に見ていただきたいです。

ライブ配信をした、他のバンドのチラシを添付します。

デザインがとても素敵だったのと
VIDDORAへの誘導が必要だったので
手に持ったスマホのデザインがとても気に入りました。

今回はたくさんの提案ありがとうございました。
こんな制度を知らなかったので、ぜひ今後とも利用しようと思いました。

```html
<!DOCTYPE html>
<html lang="ja">
<head>
<meta charset="utf-8">
<title>柳浦中学校吹奏楽部 第12回定期演奏会</title>
<link rel="stylesheet" href="https://fonts.googleapis.com/css2?family=Noto+Sans+JP:wght@400;500;700;900&family=Noto+Serif+JP:wght@600;700;900&family=Oswald:wght@500;600&display=swap">
<style>
  :root{
    --navy:#1c2452;
    --navy-deep:#141a3d;
    --red:#d6263a;
    --pink:#e8738f;
    --pink-soft:#fbe6ec;
    --gold:#d8b86a;
    --paper:#f6f3f8;
    --ink:#222638;
    --white:#ffffff;
  }
  *{margin:0;padding:0;box-sizing:border-box}
  html,body{width:849px;height:1200px;overflow:hidden;background:var(--paper)}
  body{font-family:"Noto Sans JP",sans-serif;color:var(--ink)}
  .flyer{position:relative;width:849px;height:1200px;overflow:hidden;
    background:linear-gradient(180deg,#fdfbfd 0,#f3eef5 226px,var(--navy) 226px,var(--navy) 1040px,var(--navy-deep) 1040px)}

  /* date block */
  .date{position:absolute;left:46px;top:18px;display:flex;align-items:flex-end;gap:8px;color:var(--navy)}
  .date .year{font-family:"Oswald",sans-serif;font-weight:600;font-size:34px;line-height:1;margin-bottom:10px;color:var(--red)}
  .date .day{font-family:"Oswald",sans-serif;font-weight:600;font-size:86px;line-height:.9}
  .date .dow{font-family:"Oswald",sans-serif;font-weight:500;font-size:30px;color:var(--red);margin-bottom:8px}
  .info{position:absolute;left:50px;top:118px;font-size:13px;line-height:1.55;color:var(--ink);font-weight:500}
  .info .mark{color:var(--red)}

  /* stream callout */
  .callout{position:absolute;left:512px;top:12px;width:322px;height:76px;border:3px solid var(--red);
    border-radius:14px;background:var(--white);color:var(--red);font-weight:900;font-size:18px;
    text-align:center;line-height:1.4;padding-top:9px}
  .callout::after{content:"";position:absolute;left:60px;bottom:-14px;border:12px solid transparent;
    border-top:14px solid var(--red);border-bottom:0}
  .stream{position:absolute;left:512px;top:108px;width:226px;height:92px;background:var(--navy);
    color:var(--white);text-align:center;padding-top:10px}
  .stream .channel{font-size:30px;font-weight:700;line-height:1.1}
  .stream .free{font-size:24px;font-weight:900;letter-spacing:.04em;margin-top:4px;color:var(--white)}
  .stream-arrow{position:absolute;left:738px;top:132px}
  .qr{position:absolute;left:764px;top:114px;width:76px;height:76px;background:var(--white);
    border:3px solid var(--navy);display:flex;align-items:center;justify-content:center}
  .qr span{width:54px;height:54px;background:var(--navy)}

  /* title */
  .title-box{position:absolute;left:127px;top:250px;width:595px;height:112px;border:2px solid var(--gold);
    text-align:center;color:var(--gold);font-family:"Noto Serif JP",serif}
  .title-box::before{content:"";position:absolute;inset:5px;border:1px solid var(--gold)}
  .title-box .band{font-size:24px;font-weight:700;margin-top:12px;letter-spacing:.06em}
  .title-box .event{font-size:46px;font-weight:900;line-height:1.25;letter-spacing:.04em}
  .title-box .event small{font-size:34px}

  .photo{position:absolute;background:linear-gradient(160deg,#7d6a55,#c8a87a 45%,#3e3a48)}
  .photo.stage{left:50px;top:373px;width:748px;height:244px}

  /* program */
  .program{position:absolute;left:50px;top:628px;width:748px;height:200px;background:var(--white);
    border-top:6px solid var(--pink)}
  .program h2{text-align:center;font-size:20px;font-weight:900;color:var(--red);letter-spacing:.2em;margin:8px 0 6px}
  .program .cols{display:flex;gap:18px;padding:0 22px}
  .program ul{list-style:none;flex:1;font-size:14px;line-height:1.55;font-weight:500}
  .program li{padding-left:18px;position:relative;margin-bottom:8px}
  .program li::before{content:"";position:absolute;left:0;top:6px;width:10px;height:10px;border-radius:50%;background:var(--pink)}
  .program li small{display:block;font-size:10.5px;color:#555a70;line-height:1.4;white-space:nowrap}

  .photo.row1{left:50px;top:840px;width:232px;height:150px;background:linear-gradient(160deg,#d9d4cc,#8a8f9c)}
  .photo.row2{left:289px;top:840px;width:277px;height:150px;background:linear-gradient(160deg,#3c3f5a,#b3263b 60%,#d9b27a)}
  .photo.row3{left:574px;top:840px;width:224px;height:150px;background:linear-gradient(160deg,#e7e3dd,#9a97a0)}

  .notice{position:absolute;left:50px;top:1004px;width:748px;text-align:center;color:var(--white);font-size:12.5px}

  /* footer */
  .footer{position:absolute;left:0;top:1040px;width:849px;height:160px;border-top:4px solid var(--pink);
    display:flex;align-items:center;justify-content:space-between;padding:0 46px}
  .brand{display:flex;align-items:center;gap:12px;color:var(--white);font-weight:700;font-size:22px;line-height:1.15;letter-spacing:.08em}
  .brand .dot{width:22px;height:22px;border-radius:50%;background:var(--pink)}
  .contact{color:var(--white);font-size:17px;line-height:1.6;font-weight:500}
  .contact .label{font-size:14px;color:var(--pink-soft)}
</style>
</head>
<body>
<main class="flyer">
  <div class="date"><span class="year">2020</span><span class="day">11/1</span><span class="dow">SUN</span></div>
  <p class="info">
    <span class="mark">■</span>13:00開場 ／ 13:30開演 ／ 15:00終演予定<br>
    <span class="mark">■</span>場所／ヒバリノ会館（札幌紅葉アリーナ）<br>
    主催／札幌市立柳浦中学校 吹奏楽部保護者会
  </p>

  <div class="callout">札幌市立柳浦中学校吹奏楽部<br>公式チャンネルにて！</div>
  <div class="stream">
    <div class="channel">Vidora</div>
    <div class="free">無料ライブ配信</div>
  </div>
  <svg class="stream-arrow" width="22" height="44" viewBox="0 0 22 44" aria-hidden="true"><path d="M0 0 L22 22 L0 44 Z" fill="#1c2452"/></svg>
  <div class="qr" role="img" aria-label="公式Vidoraチャンネルへの二次元コード"><span></span></div>

  <header class="title-box">
    <div class="band">札幌市立柳浦中学校吹奏楽部</div>
    <div class="event"><small>第12回</small> 定期演奏会</div>
  </header>

  <div class="photo stage" role="img" aria-label="ステージで演奏する吹奏楽部全体の写真"></div>

  <section class="program">
    <h2>プログラム</h2>
    <div class="cols">
      <ul>
        <li>第43回中央室内楽フェスタ演奏予定曲<small>「砂丘の鐘と港の夜明け」〜木管8重奏バージョン〜Tovelu作曲</small></li>
        <li>ウィンディ・ハーバー「舟と小夜子の夢渡り」より</li>
        <li>ボルディエット</li>
      </ul>
      <ul>
        <li>元気200km</li>
        <li>サクソフォンとバンドのための夏空の約束<small>〜ミルバーンズ 永遠のレパートリーより〜</small></li>
        <li>風を追って走ろうよ in swing　ほか</li>
      </ul>
    </div>
  </section>

  <div class="photo row1" role="img" aria-label="中央大会での集合写真"></div>
  <div class="photo row2" role="img" aria-label="室内楽フェスタ支部大会での演奏写真"></div>
  <div class="photo row3" role="img" aria-label="アンサンブルメンバーの舞台写真"></div>

  <p class="notice">今回の定期演奏会は、新型コロナウイルス感染予防防止の観点から、保護者・学校関係者のみの公演となりました。</p>

  <footer class="footer">
    <div class="brand"><span class="dot"></span><span>YANAGIURA<br>WIND ORCHESTRA</span></div>
    <div class="contact"><span class="label">お問い合わせ</span><br>札幌市立柳浦中学校　鹿間・楢戸・砂川（011-555-0178）</div>
  </footer>
</main>
</body>
</html>
```